The Little Sprouts Forum -Flyer Design

The flyer is for a conference that is being held for Chiropractors to gain continuing education in paediatrics with all proceeds from the event going to paediatric research.

Paediatric chiropractic is mostly about how we can help the body and brain develop optimally with a big focus of the nervous system. I have attached the logo and the website is www.littlesproutsforum.example. The feel should be kid friendly but also professional. It is also going to be largely for the American Market.

Here is an outline of the copy that we need on this flyer:
========================================
Don’t Miss This….some of the best minds in Chiropractic Pediatrics…all together in the USA.

23-24th April 2016, San Francisco. Sat 23rd 8.30-5.30 Sun 24th 8.30am -1pm

Harborview Lodge by Marwell, ​Bayline Terminal-Pierside

With all proceeds going directly to Pediatric based research projects at the Institute for Spinal Wellness Studies at QMPA.

Learn From:

Dr. Marlene Voskuil
Dr. Ingrid Wemkoss
Dr. Fabiola Trennick
Dr. Marianne Pollux
Dr. Terry Vanlund
Dr. Josephine Amsworth
Dr. Lavinia Amsworth
Dr. Greta Pomberg
Dr. Nadia Folck
Dr. Celine Marsh

Early bird $449 18th Mar 2016

CE available

More info at www.littlesproutsforum.example (could we also have a plain square icon too!)

```html
<!DOCTYPE html>
<html lang="en">
<head>
<meta charset="utf-8">
<title>The Little Sprouts Forum – Flyer</title>
<link rel="stylesheet" href="https://fonts.googleapis.com/css2?family=Antonio:wght@700&family=Oswald:wght@500;600&family=Lato:ital,wght@0,300;0,400;0,700;0,900;1,900&display=swap">
<style>
  :root {
    --orange: #f15a29;
    --green: #76a02c;
    --ink: #1d1d1b;
    --white: #ffffff;
    --footer: #414141;
    --photo-a: #e9c9a8;
    --photo-b: #f4e6d6;
  }
  * { margin: 0; padding: 0; box-sizing: border-box; }
  html, body { width: 900px; height: 1200px; overflow: hidden; background: var(--white); }
  .flyer { position: relative; width: 900px; height: 1200px; overflow: hidden; font-family: "Lato", Arial, sans-serif; }
  .backdrop { position: absolute; inset: 0; }

  .brand { position: absolute; left: 58px; top: 92px; display: flex; align-items: center; gap: 14px; }
  .brand-dot { width: 30px; height: 30px; border-radius: 50%; background: var(--orange); flex: none; }
  .brand-name { font-weight: 400; font-size: 30px; line-height: 1.05; color: var(--orange); width: 240px; }

  .divider { position: absolute; left: 358px; top: 40px; width: 4px; height: 207px; background: #3a3a3a; }

  .headline { position: absolute; left: 383px; top: 44px; text-transform: uppercase; white-space: nowrap; }
  .headline .lead { font-family: "Antonio", "Oswald", "Arial Narrow", sans-serif; font-weight: 700; font-size: 64px; line-height: 70px; color: var(--orange); letter-spacing: 0.5px; }
  .headline .line { font-family: "Oswald", "Arial Narrow", sans-serif; font-weight: 600; font-size: 28px; line-height: 42px; color: var(--ink); letter-spacing: 0.2px; }
  .headline .line.accent { color: var(--green); }

  .details { position: absolute; left: 55px; top: 410px; width: 440px; color: var(--white); }
  .ce { font-weight: 900; font-style: italic; font-size: 31px; margin-bottom: 22px; }
  .when { font-weight: 700; font-size: 20px; line-height: 1.3; text-transform: uppercase; margin-bottom: 18px; }
  .when sup { font-size: 12px; }
  .venue { font-weight: 700; font-size: 18px; line-height: 1.3; text-transform: uppercase; margin-bottom: 10px; }
  .cause { font-weight: 400; font-size: 17px; line-height: 1.35; width: 430px; }

  .price-badge { position: absolute; left: 546px; top: 417px; width: 280px; height: 280px; border-radius: 50%; background: var(--white); border: 10px solid var(--orange); text-align: center; padding-top: 54px; font-weight: 900; line-height: 1; }
  .price-badge .label { font-size: 27px; color: var(--ink); }
  .price-badge .amount { font-size: 42px; color: var(--green); margin-top: 4px; }
  .price-badge .date { font-size: 33px; color: var(--ink); margin-top: 2px; }
  .price-badge .date sup { font-size: 18px; }
  .price-badge .year { font-size: 46px; color: var(--orange); margin-top: 4px; }

  .child-photo { position: absolute; left: 560px; top: 620px; width: 330px; height: 476px; background: linear-gradient(180deg, var(--photo-b), var(--photo-a)); border-radius: 140px 140px 0 0; }

  .speakers { position: absolute; left: 0; top: 727px; width: 464px; height: 473px; background: var(--green); border-top-right-radius: 34px; padding: 36px 0 0 50px; }
  .speakers h2 { font-weight: 700; font-size: 29px; color: var(--ink); margin-bottom: 18px; }
  .speakers ul { list-style: none; }
  .speakers li { position: relative; font-size: 23px; line-height: 31px; color: var(--ink); padding-left: 32px; }
  .speakers li::before { content: ""; position: absolute; left: 0; top: 12px; width: 10px; height: 10px; border-radius: 50%; background: var(--orange); }

  .footer { position: absolute; left: 464px; top: 1096px; width: 436px; height: 104px; background: var(--footer); display: flex; align-items: center; padding-left: 22px; color: var(--white); }
  .footer .globe { width: 24px; height: 24px; flex: none; margin-right: 16px; }
  .footer .site { font-size: 17px; font-weight: 400; }
  .footer .rule { width: 2px; height: 40px; background: var(--white); margin-left: 22px; }
  .footer .social { width: 26px; height: 26px; background: var(--green); margin-left: 30px; flex: none; }
</style>
</head>
<body>
<main class="flyer">
  <svg class="backdrop" width="900" height="1200" viewBox="0 0 900 1200" aria-hidden="true">
    <path fill="var(--green)" d="M0,262 C250,300 420,325 560,305 C700,285 800,210 881,0 L900,0 L900,387 C700,380 400,335 0,275 Z"/>
    <path fill="none" stroke="var(--orange)" stroke-width="8" d="M0,262 C250,300 420,325 560,305 C700,285 800,210 881,0"/>
    <path fill="var(--green)" d="M0,320 C200,318 380,345 495,410 C625,490 725,600 785,740 L785,1200 L0,1200 Z"/>
    <path fill="var(--orange)" d="M0,322 C180,322 360,348 470,412 C600,492 700,600 760,740 L760,1200 L0,1200 Z"/>
    <rect x="760" y="700" width="140" height="400" fill="var(--white)"/>
  </svg>

  <div class="brand">
    <span class="brand-dot"></span>
    <span class="brand-name">The Little Sprouts Forum</span>
  </div>

  <div class="divider"></div>

  <header class="headline">
    <div class="lead">Don’t Miss This</div>
    <div class="line">Some of the best minds</div>
    <div class="line accent">in Chiropractic Pediatrics</div>
    <div class="line">All together in the USA</div>
  </header>

  <section class="details">
    <p class="ce">CE AVAILABLE</p>
    <p class="when">23-24<sup>th</sup> April 2016,<br>San Francisco. Sat 23rd<br>8.30-5.30 Sun 24<sup>th</sup> 8.30am -1pm</p>
    <p class="venue">Harborview Lodge by Marwell, Bayline Terminal-Pierside</p>
    <p class="cause">With all proceeds going directly to Pediatric based research projects at the Institute for Spinal Wellness Studies at QMPA.</p>
  </section>

  <div class="child-photo" role="img" aria-label="Photo of a smiling young child in a striped shirt with arms raised"></div>

  <div class="price-badge">
    <div class="label">EARLY BIRD</div>
    <div class="amount">$449</div>
    <div class="date">18<sup>th</sup> MARCH</div>
    <div class="year">2016</div>
  </div>

  <section class="speakers">
    <h2>LEARN FROM:</h2>
    <ul>
      <li>Dr. Marlene Voskuil</li>
      <li>Dr. Ingrid Wemkoss</li>
      <li>Dr. Fabiola Trennick</li>
      <li>Dr. Marianne Pollux</li>
      <li>Dr. Terry Vanlund</li>
      <li>Dr. Josephine Amsworth</li>
      <li>Dr. Lavinia Amsworth</li>
      <li>Dr. Greta Pomberg</li>
      <li>Dr. Nadia Folck</li>
      <li>Dr. Celine Marsh</li>
    </ul>
  </section>

  <footer class="footer">
    <svg class="globe" viewBox="0 0 24 24" aria-hidden="true" fill="none" stroke="#ffffff" stroke-width="1.6">
      <circle cx="12" cy="12" r="10"/>
      <ellipse cx="12" cy="12" rx="4.5" ry="10"/>
      <line x1="2" y1="12" x2="22" y2="12"/>
      <path d="M4,7 H20 M4,17 H20"/>
    </svg>
    <span class="site">www.littlesproutsforum.example</span>
    <span class="rule"></span>
    <span class="social" aria-label="Social page"></span>
  </footer>
</main>
</body>
</html>
```